Real Estate Wordpress Landing Page

I'm looking to a landing page dedicated to my real estate brokerage that's catered to promoting that my company provides 1.5% listings to home sellers... I have a couple examples that I'm really looking towards mocking in a version with similar color schemes using my current company colors/website.

http://lorvanta.com/
https://www.bluthorn.com/about/one-percent-listing-fee

My brokerage company website is http://www.calmridge.us/

Target Market(s)

real estate home sellers & buyers

Industry/Entity Type

Real Estate

Coding

Coded - Design and coding required

Number of Pages Required

1 page

Colors
3176b5
0255a3
eaf1f7
cedeed

Requirements
Must have
• Company website colors - http://www.calmridge.us/
• Something around the lines of this website page - http://lorvanta.com/
• Wordpress compatibility

```html
<!DOCTYPE html>
<html lang="en">
<head>
<meta charset="utf-8">
<title>Calmridge Realty – 1.5% Listings</title>
<link href="https://fonts.googleapis.com/css2?family=Ubuntu:wght@400;500;700&family=Open+Sans:wght@400;600;700&display=swap" rel="stylesheet">
<style>
:root{
  --blue:#0a64b8;
  --blue-dark:#0255a3;
  --blue-mid:#3176b5;
  --ice:#eaf1f7;
  --mist:#cedeed;
  --ink:#222;
  --grey:#777;
  --panel:#f3f3f3;
  --footer:#151515;
  --white:#fff;
}
*{margin:0;padding:0;box-sizing:border-box}
html,body{width:1200px;height:3593px;overflow:hidden}
body{font-family:"Open Sans",sans-serif;color:var(--ink);background:var(--white);position:relative}
.abs{position:absolute}
h2{font-family:"Ubuntu",sans-serif;font-weight:500}
/* header */
.site-header{position:absolute;left:0;top:0;width:1200px;height:165px;background:var(--white)}
.call{position:absolute;left:121px;top:70px;display:flex;align-items:center;gap:14px;font-size:11px;font-weight:700;line-height:14px}
.call .dot{width:28px;height:28px;border-radius:50%;background:var(--blue-dark);display:flex;align-items:center;justify-content:center}
.brand{position:absolute;left:500px;top:52px;width:200px;text-align:center;font-family:"Ubuntu",sans-serif;font-weight:700;font-size:26px;color:var(--blue-dark)}
.brand .mark{display:block;width:44px;height:44px;margin:0 auto 6px;background:var(--blue-dark)}
.tools{position:absolute;left:1000px;top:70px;display:flex;gap:28px}
/* hero */
.hero{position:absolute;left:0;top:165px;width:1200px;height:654px;background:linear-gradient(180deg,#7d8fa6 0%,#a39688 45%,#6c5a4b 70%,#3c4a32 100%)}
.hero-text{position:absolute;left:0;top:300px;width:1200px;text-align:center;color:var(--white);font-family:"Ubuntu",sans-serif;font-weight:700;font-size:31px;line-height:36px;text-shadow:0 2px 6px rgba(0,0,0,.4)}
.btn-ghost{position:absolute;left:484px;top:402px;width:225px;height:42px;border:2px solid var(--white);color:var(--white);font-size:14px;display:flex;align-items:center;justify-content:center;gap:12px;background:rgba(0,0,0,.25)}
/* search */
.search-band{position:absolute;left:0;top:819px;width:1200px;height:232px;background:var(--blue)}
.search-band h2{position:absolute;top:50px;width:1200px;text-align:center;color:var(--white);font-size:31px}
.field{position:absolute;top:116px;width:144px;height:38px;background:#3f86c9;color:#d6e6f5;font-size:12px;padding:0 12px;display:flex;align-items:center;justify-content:space-between}
.btn-search{position:absolute;left:915px;top:116px;width:112px;height:38px;background:#111;color:var(--white);font-size:12px;display:flex;align-items:center;justify-content:center;gap:12px}
/* sections */
.section-title{position:absolute;width:1200px;text-align:center;font-size:32px;color:var(--ink)}
.rule{position:absolute;left:530px;width:140px;height:3px;background:var(--blue-mid)}
.sub{position:absolute;width:1200px;text-align:center;font-family:"Ubuntu",sans-serif;font-size:20px}
.tabs{position:absolute;left:0;top:1198px;width:1200px;display:flex;justify-content:center;gap:34px;font-size:14px;color:#aaa}
.tabs .on{color:var(--blue-mid)}
.pager{position:absolute;left:1048px;top:1200px;display:flex;gap:6px}
.pager span{width:13px;height:13px;border-radius:50%;background:#bbb}
.pager span.on{background:var(--blue)}
.card{position:absolute;width:311px}
.card .photo{height:189px;position:relative}
.badge{position:absolute;right:10px;top:10px;background:var(--blue);color:var(--white);font-size:13px;padding:2px 14px}
.acts{position:absolute;right:8px;bottom:8px;display:flex;gap:3px}
.acts i{width:21px;height:21px;background:var(--blue)}
.card .addr{margin-top:22px;font-size:14px;line-height:19px}
.card .price{margin-top:5px;font-size:15px;font-weight:700;color:var(--blue)}
.btn-outline{position:absolute;left:522px;width:158px;height:43px;border:2px solid #111;font-size:13px;display:flex;align-items:center;justify-content:center;gap:12px}
.panel{position:absolute;left:0;width:1200px;background:var(--panel)}
/* blogs */
.post{position:absolute;top:2498px;width:319px;height:330px;background:#f4f4f4}
.post .photo{margin:0 14px;height:194px;position:relative}
.date{position:absolute;left:0;top:12px;width:36px;background:#333;color:var(--white);font-size:11px;font-weight:700;line-height:13px;padding:4px}
.post h3{margin:18px 24px 0;font-size:14px;font-weight:700}
.meta{margin:3px 24px 0;font-size:13px;font-weight:700;display:flex;gap:36px}
.post p{margin:12px 24px 0;font-size:13px;font-weight:600;line-height:16px}
.more{margin:10px 24px 0;font-size:13px;font-weight:700}
/* vendors */
.vendor{position:absolute;top:3013px;height:139px;background:var(--white);box-shadow:0 1px 6px rgba(0,0,0,.12);display:flex;align-items:center;justify-content:center;text-align:center;font-family:"Ubuntu",sans-serif;font-weight:700;font-size:20px;color:var(--blue-dark);padding:0 12px}
.arrow{position:absolute;top:3076px;width:14px;height:14px;border-radius:50%;border:1px solid #999}
/* footer */
.site-footer{position:absolute;left:0;top:3216px;width:1200px;height:377px;background:var(--footer);color:var(--white)}
.foot-logo{position:absolute;left:120px;top:40px;width:202px;height:122px;background:var(--white);display:flex;flex-direction:column;align-items:center;justify-content:center;font-family:"Ubuntu",sans-serif;font-weight:700;font-size:20px;color:var(--blue-dark)}
.foot-logo i{width:32px;height:32px;background:var(--blue-dark);margin-bottom:6px}
.about{position:absolute;left:120px;top:172px;width:205px;font-size:11px;line-height:14px}
.col h4{font-family:"Ubuntu",sans-serif;font-size:19px;font-weight:500;margin-bottom:30px}
.col{position:absolute;top:50px;font-size:11px}
.col li{list-style:none;display:flex;gap:10px;align-items:flex-start;margin-bottom:16px;line-height:14px}
.soc{width:22px;height:22px;border-radius:50%;background:var(--white);flex:none}
.col.follow li{align-items:center;margin-bottom:14px}
.subscribe{position:absolute;left:860px;top:300px;width:220px;height:30px;display:flex}
.subscribe span{flex:1;border-bottom:1px solid var(--white);font-size:11px;padding:8px 4px}
.subscribe b{width:70px;background:var(--white);color:#111;font-size:11px;font-weight:600;display:flex;align-items:center;justify-content:center}
.foot-rule{position:absolute;left:120px;top:298px;width:960px;height:1px;background:#555}
.legal{position:absolute;left:120px;top:322px;width:960px;display:flex;justify-content:space-between;font-size:11px}
.legal nav{display:flex;gap:18px}
</style>
</head>
<body>

<header class="site-header">
  <div class="call">
    <span class="dot"><svg width="14" height="14" viewBox="0 0 24 24"><path fill="#fff" d="M6.6 10.8a15 15 0 0 0 6.6 6.6l2.2-2.2c.3-.3.7-.4 1-.2 1.1.4 2.3.6 3.6.6.6 0 1 .4 1 1V20c0 .6-.4 1-1 1A17 17 0 0 1 3 4c0-.6.4-1 1-1h3.5c.6 0 1 .4 1 1 0 1.3.2 2.5.6 3.6.1.3 0 .7-.2 1z"/></svg></span>
    <span>CALL US NOW<br>+300 555 0147</span>
  </div>
  <div class="brand"><span class="mark"></span>Calmridge Realty</div>
  <div class="tools">
    <svg width="24" height="24" viewBox="0 0 24 24"><circle cx="10" cy="10" r="6" fill="none" stroke="#111" stroke-width="3"/><path d="M14.5 14.5l6 6" stroke="#111" stroke-width="4"/></svg>
    <svg width="24" height="24" viewBox="0 0 24 24"><path d="M3 5h18M3 12h18M3 19h18" stroke="#111" stroke-width="3"/></svg>
  </div>
</header>

<section class="hero" role="img" aria-label="Photo of a large tudor-style house with red tiled roof under a blue sky">
  <div class="hero-text">Find The Perfect House For You<br>And Change Your Life</div>
  <div class="btn-ghost">Brows Latets Properties <span>›</span></div>
</section>

<section class="search-band">
  <h2>Find Your Dream Home Today</h2>
  <div class="field" style="left:151px">City <span>▾</span></div>
  <div class="field" style="left:304px">Category <span>▾</span></div>
  <div class="field" style="left:457px">Type <span>▾</span></div>
  <div class="field" style="left:610px">Price Range <span>▾</span></div>
  <div class="field" style="left:764px">Area <span>▾</span></div>
  <div class="btn-search">Search <svg width="14" height="14" viewBox="0 0 24 24"><circle cx="10" cy="10" r="6" fill="none" stroke="#fff" stroke-width="3"/><path d="M14.5 14.5l6 6" stroke="#fff" stroke-width="4"/></svg></div>
</section>

<h2 class="section-title" style="top:1112px">Feature Properties</h2>
<div class="rule" style="top:1170px"></div>
<div class="tabs"><span class="on">All</span><span>Sold</span><span>Rented</span></div>
<div class="pager"><span></span><span class="on"></span></div>

<article class="card" style="left:120px;top:1248px">
  <div class="photo" role="img" aria-label="Photo of a kitchen interior with appliances" style="background:linear-gradient(135deg,#8a7a6a,#c9c2b8)"><span class="badge">Rented</span><div class="acts"><i></i><i></i><i></i></div></div>
  <div class="addr">2530 Palm Crest Boulevard 203, Bayview, FL 33445</div>
  <div class="price">$1,100/per month</div>
</article>
<article class="card" style="left:443px;top:1248px">
  <div class="photo" role="img" aria-label="Photo of a two-storey house with palm trees" style="background:linear-gradient(180deg,#8fb9e0,#d8d4c8 60%,#6f8f5a)"><span class="badge">Sold</span><div class="acts"><i></i><i></i><i></i></div></div>
  <div class="addr">10408 Willow Glen Circle, Lake Harbor, FL 33449</div>
  <div class="price">$310,000</div>
</article>
<article class="card" style="left:769px;top:1248px">
  <div class="photo" role="img" aria-label="Photo of a single-storey house with lawn" style="background:linear-gradient(180deg,#9cc3e8,#c8b9a0 60%,#6f8f5a)"><span class="badge">Sold</span><div class="acts"><i></i><i></i><i></i></div></div>
  <div class="addr">3835 Cedar Road W, Lake Harbor, FL 33467</div>
  <div class="price">$180,000</div>
</article>
<div class="btn-outline" style="top:1595px">View All <span>›</span></div>

<section class="panel" style="top:1720px;height:608px"></section>
<h2 class="section-title" style="top:1784px">List For 1.5% Commission,</h2>
<div class="sub" style="top:1834px">And Receive Top Marketing from Homeline Pro!</div>

<article class="card" style="left:120px;top:1904px">
  <div class="photo" role="img" aria-label="Photo of a modern house at dusk" style="background:linear-gradient(180deg,#6f86a8,#5a5a5a 60%,#8a6a48)"><span class="badge">Rented</span><div class="acts"><i></i><i></i><i></i></div></div>
  <div class="addr">2530 Palm Crest Boulevard 203, Bayview, FL 33445</div>
  <div class="price">$1,100/per month</div>
</article>
<article class="card" style="left:443px;top:1904px">
  <div class="photo" role="img" aria-label="Photo of a country house among trees" style="background:linear-gradient(180deg,#3f5a3a,#c9c4b8 55%,#4f7a3a)"><span class="badge">Sold</span><div class="acts"><i></i><i></i><i></i></div></div>
  <div class="addr">10408 Willow Glen Circle, Lake Harbor, FL 33449</div>
  <div class="price">$310,000</div>
</article>
<article class="card" style="left:769px;top:1904px">
  <div class="photo" role="img" aria-label="Photo of a cottage in a sunlit wood" style="background:linear-gradient(180deg,#d9c9a8,#4f5a6a 60%,#3a3a2e)"><span class="badge">Sold</span><div class="acts"><i></i><i></i><i></i></div></div>
  <div class="addr">3835 Cedar Road W, Lake Harbor, FL 33467</div>
  <div class="price">$180,000</div>
</article>
<div class="btn-outline" style="top:2232px">View All <span>›</span></div>

<h2 class="section-title" style="top:2400px">Our Blogs</h2>
<div class="sub" style="top:2450px;font-size:15px;font-weight:700;font-family:'Open Sans',sans-serif">Lorem Ipsum is simply dummy text.</div>

<article class="post" style="left:110px">
  <div class="photo" role="img" aria-label="Photo of a white villa with palm trees" style="background:linear-gradient(180deg,#c8d8ec,#e8e6e0 60%,#6f8f5a)"><span class="date">01<br>Nov</span></div>
  <h3>TV POST TITLE</h3>
  <div class="meta"><span>August 20, 2018</span><span>♡20 &nbsp; ♡ 12</span></div>
  <p>Lorem Ipsum is simply dummy text of the printing matter and typesetting industry.</p>
  <div class="more">Read More... ›</div>
</article>
<article class="post" style="left:443px">
  <div class="photo" role="img" aria-label="Photo of colourful row houses" style="background:linear-gradient(180deg,#c9d9ea,#b5654a 55%,#6a4a3a)"><span class="date">01<br>Oct</span></div>
  <h3>POST TITLE</h3>
  <div class="meta"><span>August 21, 2018</span><span>♡20 &nbsp; ♡ 12</span></div>
  <p>Lorem Ipsum is simply dummy text of the printing matter and typesetting industry.</p>
  <div class="more">Read More... ›</div>
</article>
<article class="post" style="left:776px">
  <div class="photo" role="img" aria-label="Photo of a white cottage with autumn trees" style="background:linear-gradient(180deg,#c7782e,#e8e4dc 55%,#8a7a3a)"><span class="date">01<br>Oct</span></div>
  <h3>POST TITLE</h3>
  <div class="meta"><span>August 22, 2018</span><span>♡20 &nbsp; ♡ 12</span></div>
  <p>Lorem Ipsum is simply dummy text of the printing matter and typesetting industry.</p>
  <div class="more">Read More... ›</div>
</article>

<section class="panel" style="top:2886px;height:330px;background:#f6f6f6"></section>
<h2 class="section-title" style="top:2924px">Our Vendors</h2>
<div class="rule" style="top:2978px"></div>
<span class="arrow" style="left:60px"></span>
<div class="vendor" style="left:120px;width:222px">Maple Title and Escrow Inc.</div>
<div class="vendor" style="left:364px;width:223px">Summit Home Mortgage</div>
<div class="vendor" style="left:618px;width:213px">Harbor Home Lending</div>
<div class="vendor" style="left:850px;width:225px">AllDay Notary</div>
<span class="arrow" style="left:1119px;border-color:var(--blue)"></span>

<footer class="site-footer">
  <div class="foot-logo"><i></i>Calmridge Realty</div>
  <p class="about">Calmridge Realty is a real estate brokerage company located in Coral Bend that has a team of knowledgeable real estate agents ...<br><br>Read More... ›</p>
  <div class="col" style="left:400px">
    <h4>Contact us</h4>
    <ul>
      <li><span>⌖</span><span>410 Harbor Way,<br>Ste 120, Coral Bend,<br>FL 33400</span></li>
      <li><span>✆</span><span>555-210-7930</span></li>
      <li><span>☎</span><span>555-310-0455</span></li>
      <li><span>✉</span><span>contact@calmridge.us</span></li>
    </ul>
  </div>
  <div class="col follow" style="left:592px">
    <h4>Follow Us</h4>
    <ul>
      <li><span class="soc"></span>Friendnet.com/Calmridge Realty</li>
      <li><span class="soc"></span>Chirpline.com/Calmridge Realty</li>
      <li><span class="soc"></span>Postbox.com/Calmridge Realty</li>
      <li><span class="soc"></span>Workgrid.com/Calmridge Realty</li>
    </ul>
  </div>
  <div class="col" style="left:860px;width:220px">
    <h4>Newsletter Subscribe</h4>
    <p style="line-height:14px">The Calmridge Realty team is dedicated to keeping you up to date with the real estate market.</p>
  </div>
  <div class="subscribe" style="top:250px"><span>E-mail Address</span><b>Subscribe</b></div>
  <div class="foot-rule"></div>
  <div class="legal"><span>Calmridge.us - All rights reserved.</span><nav><span>Privacy</span><span>Terms and Conditions</span><span>Contact Us</span><span>Mobile Notary</span></nav></div>
</footer>

</body>
</html>
```